Stationary and business card for an electrical contractor
Norvik Electric LLC
Stationary and business card for an electrical contractor - Construction
Creative Brief
Simple
Glen Hadley
President
412 N Orchard Ave
glen@norvikelectric-example.biz
WA Cont. # NORVIEL352TQ

```html
<!DOCTYPE html>
<html lang="en">
<head>
<meta charset="utf-8">
<title>Norvik Electric LLC – Stationery Set</title>
<link href="https://fonts.googleapis.com/css2?family=Montserrat:wght@400;600;800&display=swap" rel="stylesheet">
<style>
  :root {
    --brand-red: #e3263a;
    --brand-black: #111214;
    --paper: #ffffff;
    --canvas: #ffffff;
    --ink: #3a3a3c;
    --ink-soft: #8a8a8e;
    --shadow: 0 2px 8px rgba(0,0,0,0.18);
  }
  * { box-sizing: border-box; margin: 0; padding: 0; }
  html, body {
    width: 1200px; height: 937px; overflow: hidden;
    background: var(--canvas);
    font-family: "Montserrat", sans-serif;
    color: var(--ink);
  }
  .stationery-set { position: relative; width: 1200px; height: 937px; }
  .sheet {
    position: absolute; background: var(--paper);
    box-shadow: var(--shadow); overflow: hidden;
  }
  .wave { position: absolute; left: 0; bottom: 0; width: 100%; display: block; }
  .wave .band { fill: var(--brand-red); }
  .wave .base { fill: var(--brand-black); }

  .brand-name {
    display: inline-flex; align-items: center; gap: 0.3em;
    font-weight: 800; text-transform: uppercase; letter-spacing: 0.02em;
    color: var(--brand-black); line-height: 1;
  }
  .brand-name .brand-square {
    width: 0.8em; height: 0.8em; background: var(--brand-red); flex: none;
  }
  .brand-name.on-dark { color: #fff; }

  /* Letterhead */
  .letterhead { left: 182px; top: 71px; width: 390px; height: 541px; }
  .letterhead .brand-name { position: absolute; left: 24px; top: 26px; font-size: 13px; }
  .sender-block {
    position: absolute; right: 24px; top: 24px; text-align: right;
    font-size: 5px; line-height: 1.6; color: var(--ink-soft);
  }
  .letter-body {
    position: absolute; left: 24px; top: 90px; width: 320px;
    font-size: 5.2px; line-height: 1.75; color: var(--ink-soft);
  }
  .letter-body p { margin-bottom: 8px; }
  .signature-area {
    width: 38px; height: 14px; margin: 4px 0 6px;
    background: linear-gradient(90deg, #d8d8da, #efeff0);
  }
  .letter-sign strong { color: var(--ink); font-weight: 600; display: block; }
  .letter-footer {
    position: absolute; left: 24px; top: 424px;
    font-size: 5px; color: var(--ink-soft);
  }

  /* Second sheet */
  .cover-sheet { left: 633px; top: 35px; width: 460px; height: 582px; }
  .cover-sheet .brand-name {
    position: absolute; left: 50%; top: 215px; transform: translateX(-50%);
    font-size: 30px; white-space: nowrap;
  }

  /* Business cards */
  .card { width: 149px; height: 94px; left: 84px; }
  .card-front { top: 663px; }
  .card-front .brand-name { position: absolute; left: 10px; top: 10px; font-size: 7.5px; }
  .card-details {
    position: absolute; left: 10px; top: 30px;
    font-size: 3.6px; line-height: 1.6; color: var(--ink-soft);
  }
  .card-details strong { color: var(--ink); font-weight: 600; font-size: 4.4px; }
  .card-back { top: 772px; height: 111px; background: var(--brand-black); }
  .card-back .brand-name {
    position: absolute; left: 50%; top: 50%; transform: translate(-50%, -50%);
    font-size: 11px; white-space: nowrap;
  }

  /* Envelopes */
  .envelope-front { left: 268px; top: 663px; width: 456px; height: 220px; }
  .envelope-front .brand-name { position: absolute; left: 20px; top: 22px; font-size: 14px; }
  .envelope-back { left: 739px; top: 673px; width: 451px; height: 210px; }
  .envelope-flap { position: absolute; left: 0; top: 0; width: 100%; height: 110px; }
  .envelope-flap path { fill: var(--brand-black); }
  .web-address {
    position: absolute; left: 0; right: 0; top: 30px; text-align: center;
    color: #fff; font-size: 10px; letter-spacing: 0.28em; font-weight: 400;
  }
</style>
</head>
<body>
<main class="stationery-set">

  <!-- Letterhead -->
  <section class="sheet letterhead">
    <span class="brand-name"><span class="brand-square"></span>Norvik Electric</span>
    <address class="sender-block">
      412 N Orchard Ave<br>
      Spokane, WA 99201<br>
      (509) 555-0142<br>
      glen@norvikelectric-example.biz
    </address>
    <div class="letter-body">
      <p>July 8, 2024</p>
      <p>Dear Client,<br>Re: Project Proposal</p>
      <p>Thank you for choosing our team for your electrical needs. We handle wiring, panel upgrades, lighting and service calls for homes and businesses across the region with care and safety first.</p>
      <p>Our licensed crew will review the site, confirm the scope and send a clear written estimate before any work begins.</p>
      <p>Please call us with any questions. We look forward to working with you.</p>
      <div class="letter-sign">
        Best regards,
        <div class="signature-area" role="img" aria-label="Handwritten signature"></div>
        <strong>Glen Hadley</strong>
        President
      </div>
    </div>
    <div class="letter-footer">412 N Orchard Ave</div>
    <svg class="wave" viewBox="0 0 400 62" preserveAspectRatio="none" height="62" aria-hidden="true">
      <path class="band" d="M0,18 C120,58 260,8 400,0 L400,12 C260,20 120,70 0,34 Z"/>
      <path class="base" d="M0,34 C120,70 260,20 400,12 L400,62 L0,62 Z"/>
    </svg>
  </section>

  <!-- Second sheet -->
  <section class="sheet cover-sheet">
    <span class="brand-name"><span class="brand-square"></span>Norvik Electric</span>
    <svg class="wave" viewBox="0 0 400 72" preserveAspectRatio="none" height="72" aria-hidden="true">
      <path class="band" d="M0,20 C120,66 260,10 400,0 L400,14 C260,24 120,80 0,38 Z"/>
      <path class="base" d="M0,38 C120,80 260,24 400,14 L400,72 L0,72 Z"/>
    </svg>
  </section>

  <!-- Business card front -->
  <section class="sheet card card-front">
    <span class="brand-name"><span class="brand-square"></span>Norvik Electric</span>
    <div class="card-details">
      <strong>Glen Hadley</strong><br>
      President<br>
      412 N Orchard Ave<br>
      (509) 555-0142<br>
      glen@norvikelectric-example.biz<br>
      WA Cont. # NORVIEL352TQ
    </div>
    <svg class="wave" viewBox="0 0 400 60" preserveAspectRatio="none" height="18" aria-hidden="true">
      <path class="band" d="M0,18 C120,58 260,8 400,0 L400,14 C260,22 120,70 0,34 Z"/>
      <path class="base" d="M0,34 C120,70 260,22 400,14 L400,60 L0,60 Z"/>
    </svg>
  </section>

  <!-- Business card back -->
  <section class="sheet card card-back">
    <span class="brand-name on-dark"><span class="brand-square"></span>Norvik Electric</span>
  </section>

  <!-- Envelope front -->
  <section class="sheet envelope-front">
    <span class="brand-name"><span class="brand-square"></span>Norvik Electric</span>
    <svg class="wave" viewBox="0 0 400 60" preserveAspectRatio="none" height="58" aria-hidden="true">
      <path class="band" d="M0,16 C120,56 260,8 400,0 L400,12 C260,20 120,68 0,32 Z"/>
      <path class="base" d="M0,32 C120,68 260,20 400,12 L400,60 L0,60 Z"/>
    </svg>
  </section>

  <!-- Envelope back -->
  <section class="sheet envelope-back">
    <svg class="envelope-flap" viewBox="0 0 451 110" preserveAspectRatio="none" aria-hidden="true">
      <path d="M0,0 H451 V62 Q225,110 0,62 Z"/>
    </svg>
    <div class="web-address">www.norvikelectric-example.com</div>
  </section>

</main>
</body>
</html>
```